company letterhead and quote form

Design a company letterhead for liquid waste company. Design must be around the company image and logos provided. I need this as a working word template and must be compatible to word 2013.
Also using same letterhead design, provide a quote template.
Info on the letterhead must have - address and stuff -
47 Brackwell Rd Para Hills West SA 5096. Ph 08 8413 2957, Fax 08 8472 6190. ABN 57 304 226 718, it might be good to put the services we do on it as well.
The business card is to have logo, address and stuff and services that we do - Grease Trap Service, Septic and Aerobic cleaning, Trade Waste Cartage, Oily Water removal, Winery Waste Water.

Look at www.harbellfluidservices.com for a general feel of everything.

```html
<!DOCTYPE html>
<html lang="en">
<head>
<meta charset="utf-8">
<title>Harbell Fluid Services – Stationery</title>
<link href="https://fonts.googleapis.com/css2?family=Montserrat:wght@600;700&family=Source+Sans+3:wght@400;600;700&display=swap" rel="stylesheet">
<style>
:root{
  --navy:#221d56;
  --orange:#f05a22;
  --stage:#a8a8a8;
  --ink:#222;
  --cell:#d6d4ea;
  --white:#fff;
}
*{box-sizing:border-box;margin:0;padding:0}
html,body{width:1200px;height:640px;overflow:hidden;background:var(--stage);font-family:"Source Sans 3",Arial,sans-serif;color:var(--ink)}
.canvas{position:relative;width:1200px;height:640px}
.sheet{position:absolute;top:20px;width:314px;height:442px;background:var(--white);box-shadow:10px 12px 10px rgba(0,0,0,.45)}
.sheet-1{left:37px}.sheet-2{left:442px}.sheet-3{left:854px}
.masthead{height:49px;background:var(--navy);border-bottom:4px solid var(--orange);position:relative;color:var(--white)}
.brand{position:absolute;left:24px;top:16px;display:flex;align-items:center;gap:4px;font-weight:700;font-size:7.5px;letter-spacing:.3px;color:var(--white)}
.brand i{width:10px;height:10px;border-radius:50%;background:var(--orange);display:block}
.mast-id{position:absolute;left:169px;top:16px;font-size:4.3px;text-align:right;line-height:1.35;width:72px}
.mast-rule{position:absolute;left:245px;top:12px;width:.6px;height:27px;background:#8b87b5}
.mast-contact{position:absolute;left:251px;top:14px;font-size:4.3px;line-height:1.35}
.mast-contact b{font-weight:700}
.footband{position:absolute;left:0;right:0;bottom:0;height:11px;background:var(--navy);border-top:3px solid var(--orange)}
.folio{position:absolute;bottom:20px;left:17px;right:36px;display:flex;justify-content:space-between;font-size:4.3px}
.body{position:absolute;left:28px;right:26px;top:70px;font-size:5.3px;line-height:1.45}
.quote-to h2{font-family:Montserrat,sans-serif;font-size:7.5px;color:var(--navy);margin-bottom:4px}
.quote-to p{font-size:4.6px;line-height:1.5}
.quote-meta{position:absolute;left:166px;top:-2px;font-size:4.6px;line-height:2}
.quote-meta span{display:inline-block;width:40px;font-weight:600}
.dash{border-top:.8px dashed #999;margin:12px -12px 6px}
.body h1{font-family:Montserrat,sans-serif;font-size:8.6px;color:#111;margin-bottom:6px}
.body p{margin-bottom:6px}
.rates{width:100%;border-collapse:separate;border-spacing:1px;border-top:2px solid var(--orange);margin:2px 0 14px}
.rates th{background:var(--navy);color:var(--white);font-size:4.6px;font-weight:600;height:7px}
.rates td{background:var(--cell);height:27px}
.notes h3{font-size:6px;color:var(--navy);font-weight:700}
.notes p{font-size:3.6px;line-height:1.4}
.banner{background:var(--orange);color:var(--white);font-family:Montserrat,sans-serif;font-weight:700;font-size:5.4px;white-space:nowrap;text-align:center;padding:2px 0;width:258px;margin:16px 0 8px 4px}
.testimonial{font-size:4.9px;line-height:1.5;margin-bottom:8px}
.testimonial q{font-weight:600;quotes:"\201C" "\201D"}
.signoff{position:absolute;left:16px;right:16px;top:386px;border-top:.8px dashed #999;display:flex;justify-content:space-between;padding:3px 40px 0 31px;font-size:5.2px;font-weight:700;color:var(--navy)}
.card{position:absolute;top:494px;width:197px;height:120px;box-shadow:8px 8px 8px rgba(0,0,0,.45);overflow:hidden}
.card-a{left:37px}.card-b{left:267px}.card-c{left:500px}.card-d{left:735px}.card-e{left:970px}
.navy{background:var(--navy);color:var(--white)}
.light{background:var(--white);color:var(--ink)}
.person{font-family:Montserrat,sans-serif}
.person strong{display:block;font-size:7px;font-weight:600}
.person small{display:block;font-size:5px;font-family:"Source Sans 3",sans-serif}
.light .person strong{color:var(--navy)}
.card-e .side .person strong{color:var(--white)}
.contacts{font-size:4.9px;line-height:1.5}
.contacts li{list-style:none;display:flex;align-items:center;gap:3px}
.contacts li svg{width:5px;height:5px;fill:var(--orange);flex:none}
.contacts .gap{margin-top:4px}
.contacts address{font-style:normal;margin-top:5px;line-height:1.3}
.card-brand{display:flex;align-items:center;gap:4px;font-weight:700;font-size:8px;color:var(--white);white-space:nowrap}
.card-brand i{width:14px;height:14px;border-radius:50%;background:var(--orange);display:block;flex:none}
.card-a .top{height:48px;text-align:center;padding-top:22px}
.card-a .bottom{position:absolute;top:48px;left:0;right:0;bottom:0;background:var(--navy);color:var(--white)}
.card-a .card-brand{position:absolute;left:16px;top:28px;font-size:7px}
.card-a .contacts{position:absolute;left:112px;top:12px}
.card-b .person,.card-c .person{position:absolute;left:15px;top:26px}
.card-b .contacts,.card-c .contacts{position:absolute;left:15px;top:53px}
.card-d .card-brand{position:absolute;left:42px;top:50px;font-size:11px}
.card-d .card-brand i{width:20px;height:20px}
.card-e .side{position:absolute;left:98px;top:0;bottom:0;right:0;background:var(--navy);color:var(--white)}
.card-e .person{position:absolute;left:20px;top:14px}
.card-e .card-brand{position:absolute;left:12px;top:82px;font-size:7px}
.card-e .contacts{position:absolute;left:13px;top:53px}
</style>
</head>
<body>
<svg width="0" height="0" style="position:absolute" aria-hidden="true">
  <symbol id="i-phone" viewBox="0 0 10 10"><path d="M2 1l2 2-1 1.2c.6 1.2 1.6 2.2 2.8 2.8L7 6l2 2-1.3 1.3C4.5 9 1 5.5.7 2.3z"/></symbol>
  <symbol id="i-mail" viewBox="0 0 10 10"><path d="M1 2h8v6H1z"/></symbol>
  <symbol id="i-web" viewBox="0 0 10 10"><circle cx="5" cy="5" r="4.2"/></symbol>
</svg>

<div class="canvas">

  <section class="sheet sheet-1">
    <header class="masthead">
      <div class="brand"><i></i>HARBELL FLUID</div>
      <div class="mast-id">Harbell Fluid Services Pty Ltd<br>ABN 57 304 226 718</div>
      <div class="mast-rule"></div>
      <div class="mast-contact">08 8413 2957<br>08 8472 6190<br><b>47 Brackwell Rd Kelford Heights<br>SA 5187</b></div>
    </header>
    <div class="body">
      <div class="quote-to">
        <h2>Quote To:</h2>
        <p><b>Mr. Evan Roderick</b><br>3/52 Tarrow Road, Cityxxxx, PO BOX 0000<br>Phone: 000 0000 00</p>
      </div>
      <div class="quote-meta">
        <div><span>Quote #:</span>XX123456789</div>
        <div><span>Validity Period:</span>00.00.0000-00.00.0000</div>
        <div><span>Expire Date:</span>00.00.0000</div>
      </div>
      <div class="dash"></div>
      <h1>Proposal for your Liquid Waste Removal.</h1>
      <p>First of all thank you for your time in allowing me to put a proposal together for your liquid waste removal solution.</p>
      <p>A little about our company. We are YOUR Local, Reliable, South Australian Family Owned and Operated liquid waste company with over 20 years of experience in the industry. Whether you need a tiny truck for tight access or you need ‘The Big One’, we have a fleet of vehicles at your disposal. Harbell has the equipment and the manpower with a ‘Can do Attitude’ to get the job done. Harbell Fluid Services is a fully certified, OH&amp;S compliant and EPA licensed company. We can pump out and transport and dispose of all commercial, retail, hospitality, industrial and domestic liquid wastes and sludges. Our services are designed to help you save money, save on lost production and down time and comply with strict requirements as set out by the State Water Board.</p>
      <p>Your investment for this service will be as follows:</p>
      <table class="rates">
        <thead><tr><th style="width:29%">Service Type</th><th>Size</th><th>Frequency</th><th>Access</th><th style="width:20%">Service Charge</th><th>Collection</th></tr></thead>
        <tbody><tr><td></td><td></td><td></td><td></td><td></td><td></td></tr><tr><td></td><td></td><td></td><td></td><td></td><td></td></tr><tr><td></td><td></td><td></td><td></td><td></td><td></td></tr></tbody>
      </table>
      <p>The ‘Harbell Crew’ as they are known in the industry have a ‘CAN DO GET THE JOB DONE’ attitude and instil old fashioned work ethics throughout their fully trained team. From the time our friendly staff receive your call, to the handshake and introduction of the sales department, to the time that you are serviced by our reliable drivers and reliable modern fleet, every small detail is dealt with and accounted for.</p>
      <p>Five star customer service is what sets Harbell Fluid Services apart from our competition.<br>Harbell prides itself on providing our clients with open communication, dedication, quality and satisfaction on every service provided. This means NO call centres and NO interstate sales or accounts management.</p>
    </div>
    <div class="folio"><span>00/00/2015</span><span>Page 1 of 2</span></div>
    <div class="footband"></div>
  </section>

  <section class="sheet sheet-2">
    <header class="masthead">
      <div class="brand"><i></i>HARBELL FLUID</div>
      <div class="mast-id">Harbell Fluid Services Pty Ltd<br>ABN 57 304 226 718</div>
      <div class="mast-rule"></div>
      <div class="mast-contact">08 8413 2957<br>08 8472 6190<br><b>47 Brackwell Rd Kelford Heights<br>SA 5187</b></div>
    </header>
    <div class="body" style="top:64px;left:26px">
      <div class="notes">
        <h3>Notes:</h3>
        <p>Space for any further notes on this quote, including site access, preferred service times, pump out volumes, disposal points and any special handling needs agreed with the client before work begins.</p>
      </div>
      <div class="banner">DON’T BELIEVE US? HERE IS WHAT SOME OF OUR CUSTOMERS HAVE SAID</div>
      <p class="testimonial"><q>CWR has utilised Harbell Fluid Services since 2006. Their service has always been prompt and efficient enabling us to meet the often stringent needs of our clients with confidence. Whether waste water plant pump outs or removal of oily waste, Harbell have always met our needs and expectations.</q></p>
      <p class="testimonial"><b>Lena Hartigan</b>, Value Creation Manager, Clearwater Reclaim.</p>
      <p class="testimonial"><q>We service and repair Septic and Aerobic waste water systems for over 2500 clients throughout South Australia. The Harbell crew are very reliable and make it easy for our technicians by arranging specific service appointment times and sticking to them.</q></p>
      <p class="testimonial"><b>Dora Whitcombe</b>, Managing Director, Ridgeline Septic Care.</p>
      <p class="testimonial"><q>Calder operate the largest privately owned scrap metal recycling company in SA. We want to support local SA business and we want to deal with the decision makers. Harbell were able to handle all of our oily water and septic quickly and economically. I am happy to recommend The Harbell Service to others.</q></p>
      <p class="testimonial"><b>Neil Prowse</b>, Director, Calder Metal Recyclers.</p>
    </div>
    <div class="signoff"><span>Signature</span><span>Date</span></div>
    <div class="folio"><span>00/00/2015</span><span>Page 2 of 2</span></div>
    <div class="footband"></div>
  </section>

  <section class="sheet sheet-3">
    <header class="masthead">
      <div class="brand"><i></i>HARBELL FLUID</div>
      <div class="mast-id">Harbell Fluid Services Pty Ltd<br>ABN 57 304 226 718</div>
      <div class="mast-rule"></div>
      <div class="mast-contact">08 8413 2957<br>08 8472 6190<br><b>47 Brackwell Rd Kelford Heights<br>SA 5187</b></div>
    </header>
    <div class="footband"></div>
  </section>

  <article class="card card-a light">
    <div class="top person"><strong>Corin Lathey</strong><small>Executive</small></div>
    <div class="bottom">
      <div class="card-brand"><i></i>HARBELL FLUID</div>
      <ul class="contacts">
        <li><svg><use href="#i-phone"/></svg>08 8413 2957</li>
        <li><svg><use href="#i-phone"/></svg>08 8472 6190</li>
        <li class="gap"><svg><use href="#i-mail"/></svg>info@harbellfluid.com.au</li>
        <li><svg><use href="#i-web"/></svg>www.harbellfluid.com.au</li>
        <address>47 Brackwell Rd Kelford Heights<br>SA 5187</address>
      </ul>
    </div>
  </article>

  <article class="card card-b navy">
    <div class="person"><strong>Corin Lathey</strong><small>Executive</small></div>
    <ul class="contacts">
      <li><svg><use href="#i-phone"/></svg>08 8413 2957</li>
      <li><svg><use href="#i-phone"/></svg>08 8472 6190</li>
      <li class="gap"><svg><use href="#i-mail"/></svg>info@harbellfluid.com.au</li>
      <li><svg><use href="#i-web"/></svg>www.harbellfluid.com.au</li>
      <address>47 Brackwell Rd Kelford Heights<br>SA 5187</address>
    </ul>
  </article>

  <article class="card card-c light">
    <div class="person"><strong>Corin Lathey</strong><small>Executive</small></div>
    <ul class="contacts">
      <li><svg><use href="#i-phone"/></svg>08 8413 2957</li>
      <li><svg><use href="#i-phone"/></svg>08 8472 6190</li>
      <li class="gap"><svg><use href="#i-mail"/></svg>info@harbellfluid.com.au</li>
      <li><svg><use href="#i-web"/></svg>www.harbellfluid.com.au</li>
      <address>47 Brackwell Rd Kelford Heights<br>SA 5187</address>
    </ul>
  </article>

  <article class="card card-d navy">
    <div class="card-brand"><i></i>HARBELL FLUID</div>
  </article>

  <article class="card card-e light">
    <ul class="contacts">
      <li><svg><use href="#i-phone"/></svg>08 8413 2957</li>
      <li><svg><use href="#i-phone"/></svg>08 8472 6190</li>
      <li class="gap"><svg><use href="#i-mail"/></svg>info@harbellfluid.com.au</li>
      <li><svg><use href="#i-web"/></svg>www.harbellfluid.com.au</li>
      <address>47 Brackwell Rd Kelford Heights<br>SA 5187</address>
    </ul>
    <div class="side">
      <div class="person"><strong>Corin Lathey</strong><small>Executive</small></div>
      <div class="card-brand"><i></i>HARBELL</div>
    </div>
  </article>

</div>
</body>
</html>
```